Design Shopify E-Commerce Website for Men's Products

Design a Shopify website for men to sell our men's jewelry, cigar and bar accessories, and other men's products. Design should be hip, with like a rock n' roll, biker, whiskey driker flare. Name of the company is "Outlaw Cupboard" and website will be www.OutlawCupboard.com
Homepage will have navigation bar with three categories: Men's Jewelry, Cigar & Bar Products, Man Cave Swag
I will upload our logo, inspiration type pictures and some of the products that we sell
Theme colors should be mainly dark: black, grey, brown, gold

```html
<!DOCTYPE html>
<html lang="en">
<head>
<meta charset="utf-8">
<title>Outlaw Cupboard</title>
<link href="https://fonts.googleapis.com/css2?family=Lato:wght@400;700;900&family=UnifrakturMaguntia&display=swap" rel="stylesheet">
<style>
:root{
  --black:#000;
  --panel:#0b0b0b;
  --card:#111;
  --line:#2a2a2a;
  --gold:#d9b95c;
  --gold-soft:#e6c76a;
  --text:#e8e8e8;
  --muted:#a9a9a9;
  --brown:#3a2414;
}
*{margin:0;padding:0;box-sizing:border-box}
html,body{width:1200px;height:4422px;overflow:hidden;background:var(--black)}
body{position:relative;font-family:"Lato",sans-serif;color:var(--text)}
.abs{position:absolute}
.blackletter{font-family:"UnifrakturMaguntia",serif;font-weight:400;color:var(--text)}
.gold{color:var(--gold)}
.section-title{position:absolute;left:0;width:1200px;text-align:center;font-size:44px}
.ornament{position:absolute;left:460px;width:280px;height:26px;background:linear-gradient(90deg,transparent,var(--gold) 20%,var(--gold) 80%,transparent);clip-path:polygon(0 46%,45% 46%,50% 0,55% 46%,100% 46%,100% 56%,55% 56%,50% 100%,45% 56%,0 56%)}
.btn-outline{position:absolute;border:1.5px solid var(--gold);color:var(--gold);font-size:11px;font-weight:700;letter-spacing:.5px;text-transform:uppercase;display:flex;align-items:center;justify-content:center}
.photo{position:absolute}

/* header */
.topbar{position:absolute;top:16px;right:40px;font-size:11px;font-weight:700;display:flex;gap:30px;align-items:center;color:var(--text)}
.topbar a{color:var(--gold);text-decoration:underline}
.brand{position:absolute;left:30px;top:40px;font-size:16px;font-weight:900;color:var(--gold);display:flex;align-items:center;gap:8px}
.brand i{width:12px;height:12px;background:var(--gold);display:block}
.nav{position:absolute;left:292px;top:58px;display:flex;gap:26px;font-size:11.5px;font-weight:700;text-transform:uppercase}
.nav .active{color:var(--gold);border-bottom:1.5px solid var(--gold);padding-bottom:3px}
.tools{position:absolute;left:1028px;top:56px;display:flex;gap:16px;font-size:11px;font-weight:700;align-items:center}

/* hero */
.hero-photo{left:0;top:0;width:1200px;height:673px;background:radial-gradient(ellipse at 80% 55%,#7a3c10 0%,#3b1b08 25%,#120905 55%,#000 80%);clip-path:polygon(0 0,1200px 0,1200px 575px,1082px 673px,0 567px)}
.tag{left:120px;top:251px;height:24px;padding:0 14px;background:#8c7330;color:#111;font-size:13px;font-weight:700;display:flex;align-items:center}
.hero-title{left:120px;top:285px;font-size:52px}
.hero-sub{left:120px;top:354px;font-size:17px;color:#ddd}

/* categories */
.cat{position:absolute;top:865px;height:406px;border-radius:4px;overflow:hidden}
.cat .label{position:absolute;left:22px;bottom:20px;font-size:18px;font-weight:700;text-transform:uppercase}

/* newsletter */
.news-photo{left:0;top:0;width:1200px;height:4422px;background:linear-gradient(90deg,#2c3440 0%,#4b4d52 35%,#6a5a4c 55%,#2e3a44 100%);clip-path:polygon(0 1477px,120px 1348px,1200px 1425px,1200px 1717px,1082px 1794px,0 1648px)}
.email-box{left:312px;top:1595px;width:576px;height:43px;border:1.5px solid #ddd;display:flex;align-items:center;justify-content:space-between;padding:0 16px;font-size:13px;background:rgba(0,0,0,.25)}

/* products */
.product{position:absolute;top:1983px;width:222px;height:292px;border:1px solid var(--line);background:var(--panel);text-align:center}
.product .img{position:absolute;left:0;top:0;width:220px;height:220px}
.product .name{position:absolute;left:0;right:0;top:240px;font-size:13px;font-weight:700;text-transform:uppercase}
.product .price{position:absolute;left:0;right:0;top:266px;font-size:12px;font-weight:700;color:var(--gold)}
.product .price s{color:#777;font-weight:400}
.badge{position:absolute;left:10px;top:10px;padding:3px 7px;font-size:8px;font-weight:900;text-transform:uppercase}
.basket{position:absolute;left:0;top:186px;width:220px;height:34px;background:var(--gold);color:#fff;font-size:9px;font-weight:700;display:flex;align-items:center;justify-content:center}

/* about */
.about-band{left:0;top:0;width:1200px;height:4422px;background:#0c0c0c;clip-path:polygon(0 2524px,120px 2421px,1200px 2533px,1200px 3133px,1082px 3197px,0 3082px)}
.about-frame{left:120px;top:2507px;width:421px;height:524px;border:1px solid #2e2e2e}
.about-text{left:639px;top:2693px;width:440px;font-size:13.5px;line-height:22.5px;color:#d0d0d0;text-align:justify}
.about-text p+p{margin-top:22px}

/* news */
.post{position:absolute;top:3388px;width:304px;height:415px;background:var(--panel);border:1px solid #1c1c1c;text-align:center;overflow:hidden}
.post .img{position:absolute;left:0;top:0;width:302px;height:283px}
.post h3{position:absolute;top:310px;left:34px;right:34px;font-size:16.5px;line-height:22.5px;font-weight:700}
.post time{position:absolute;display:block;left:0;right:0;top:383px;font-size:10.5px;font-weight:700;letter-spacing:.5px;color:var(--gold);text-align:center}
.post.featured{background:var(--gold)}
.post.featured h3{color:#fff}
.post.featured time{color:#3a2d10}

/* footer */
.footer-photo{left:0;top:0;width:1200px;height:4422px;background:linear-gradient(180deg,#2a1a10 0%,#1a110a 50%,#0d0805 100%);clip-path:polygon(0 4078px,120px 3949px,1200px 4026px,1200px 4422px,0 4422px)}
.foot-brand{left:120px;top:4130px;font-size:18px;font-weight:900;color:var(--gold);display:flex;align-items:center;gap:8px}
.foot-brand i{width:14px;height:14px;background:var(--gold);display:block}
.foot-contact{left:120px;font-size:13px;display:flex;align-items:center;gap:12px}
.foot-head{font-size:18px;font-weight:700;text-transform:uppercase}
.links{left:366px;top:4120px;font-size:11.5px;font-weight:700;line-height:24px;text-transform:uppercase}
.links .active{color:var(--gold);text-decoration:underline}
.field{position:absolute;border-bottom:1px solid #6a6a6a;font-size:11px;color:#aaa;height:22px}
.field small{position:absolute;top:-14px;font-size:8px;color:#ccc}
.copy{left:120px;top:4392px;font-size:11.5px}
.copy a{color:var(--gold);text-decoration:underline}
.legal{left:610px;top:4392px;font-size:11.5px}
.social{left:992px;top:4393px;display:flex;gap:14px}
.social i{display:block;width:10px;height:10px;border-radius:50%;background:#ddd}
</style>
</head>
<body>

<!-- hero -->
<div class="photo hero-photo" role="img" aria-label="Smoky dark scene with a lit cigar and whiskey being poured into a glass of ice"></div>
<svg class="abs" style="left:0;top:0" width="1200" height="700"><polyline points="0,567 1082,673 1200,575" fill="none" stroke="var(--gold)" stroke-width="4"/></svg>

<div class="topbar">
  <span>&#9743;&nbsp; OUR PHONE NUMBER: <a>+01 (555) 010 274</a></span>
  <span>&#9711;&nbsp; LOGIN / REGISTER</span>
</div>
<div class="brand"><i></i>Outlaw Cupboard</div>
<nav class="nav">
  <span class="active">Home</span><span>About Us</span><span>Men's Jewelry</span><span>Cigar &amp; Bar</span><span>Man Cave Swag</span><span>Shop</span><span>News</span><span>Contact Us</span>
</nav>
<div class="tools">
  <svg width="14" height="14"><circle cx="6" cy="6" r="4.5" fill="none" stroke="#fff" stroke-width="1.6"/><line x1="9.5" y1="9.5" x2="13" y2="13" stroke="#fff" stroke-width="1.6"/></svg>
  <svg width="14" height="14"><path d="M7 12 L2 7 A3 3 0 0 1 7 3 A3 3 0 0 1 12 7 Z" fill="none" stroke="#fff" stroke-width="1.5"/></svg>
  <span style="display:flex;gap:6px;align-items:center"><svg width="16" height="14"><path d="M1 2h3l2 8h8l1.5-6H5" fill="none" stroke="#fff" stroke-width="1.5"/><circle cx="7" cy="12.5" r="1.2" fill="#fff"/><circle cx="13" cy="12.5" r="1.2" fill="#fff"/></svg>0 / $0.00</span>
</div>

<div class="abs tag">YOUR FAVORITE</div>
<h1 class="abs blackletter hero-title"><span class="gold">Outlaw Cupboard</span> Store</h1>
<p class="abs hero-sub">All our products are genuine, not counterfeit</p>
<div class="btn-outline" style="left:120px;top:398px;width:120px;height:35px">Shop Now!</div>

<!-- categories -->
<h2 class="blackletter section-title" style="top:740px">Shop by Category</h2>
<div class="ornament" role="img" aria-label="Gold scroll ornament" style="top:811px"></div>
<div class="cat" style="left:120px;width:304px;background:linear-gradient(160deg,#8a8a8a,#2e2e2e 70%,#1a1a1a)" role="img" aria-label="Black and white portrait of a man in sunglasses wearing rings and a watch"><span class="label">Men's Jewelry</span></div>
<div class="cat" style="left:457px;width:288px;background:radial-gradient(circle at 50% 40%,#8a5a22,#3a2210 55%,#150c06)" role="img" aria-label="Glass of whiskey with a cigar on a wooden table"><span class="label" style="bottom:50px">Cigar &amp; Bar</span><span class="label" style="bottom:14px;font-size:20px">&#8594;</span></div>
<div class="cat" style="left:774px;width:304px;background:linear-gradient(160deg,#6f6f6f,#3a3a3a 55%,#141414)" role="img" aria-label="Black and white photo of a man in a hat exhaling smoke"><span class="label">Man Cave Swag</span></div>

<!-- newsletter -->
<div class="photo news-photo" role="img" aria-label="Close-up of a tattooed man wearing bracelets, rings and a pendant"></div>
<svg class="abs" style="left:0;top:1330px" width="1200" height="480"><polyline points="0,147 120,18 1200,95" fill="none" stroke="var(--gold)" stroke-width="4"/><polyline points="0,318 1082,464 1200,387" fill="none" stroke="var(--gold)" stroke-width="4"/></svg>
<h2 class="blackletter section-title" style="top:1497px">Sign up our newsletter</h2>
<p class="abs" style="left:0;width:1200px;text-align:center;top:1554px;font-size:14px">Subscribe our newsletters now and stay up-to-date with new collections</p>
<div class="abs email-box"><span>Enter Your Email...</span><span style="font-size:18px">&#8594;</span></div>

<!-- featured products -->
<h2 class="blackletter section-title" style="top:1865px">Featured Products</h2>
<div class="ornament" role="img" aria-label="Gold scroll ornament" style="top:1932px"></div>

<div class="product" style="left:120px">
  <div class="img" role="img" aria-label="Cigar beside a glass of whiskey" style="background:radial-gradient(circle at 60% 40%,#7a4a1c,#2a1a0c 70%)"></div>
  <span class="badge" style="background:var(--gold);color:#fff">Sale</span>
  <div class="name">Cigarbar</div><div class="price">$34.00</div>
</div>
<div class="product" style="left:366px">
  <div class="img" role="img" aria-label="Silver and gold cross signet ring" style="background:radial-gradient(circle,#b8b8b8,#f4f4f4 60%,#fff)"></div>
  <div class="basket"><span style="position:absolute;left:14px">&#9825;</span>ADD TO BASKET<span style="position:absolute;right:14px">&#9673;</span></div>
  <div class="name">Heavyring</div><div class="price">$15.00</div>
</div>
<div class="product" style="left:611px">
  <div class="img" role="img" aria-label="Wooden desktop cigar cutter" style="background:radial-gradient(circle at 50% 55%,#8a4a1e,#c8c0b6 70%,#e6e1da)"></div>
  <span class="badge" style="background:#111;color:#fff">New</span>
  <div class="name">Cigarcutter</div><div class="price">$38.00</div>
</div>
<div class="product" style="left:857px">
  <div class="img" role="img" aria-label="Silver cross pendant" style="background:radial-gradient(circle,#9a9a9a,#f0f0f0 55%,#fff)"></div>
  <span class="abs" style="right:12px;top:0;width:24px;height:44px;background:var(--gold);clip-path:polygon(0 0,100% 0,100% 100%,50% 80%,0 100%)"></span>
  <div class="name">Pendantresized</div><div class="price"><s>$50.00</s> - $35.00</div>
</div>
<div class="btn-outline" style="left:541px;top:2308px;width:118px;height:34px">View All</div>

<!-- about -->
<div class="photo about-band"></div>
<svg class="abs" style="left:0;top:2410px" width="1200" height="800"><polyline points="0,114 120,11 1200,123" fill="none" stroke="var(--gold)" stroke-width="4"/><polyline points="0,672 1082,787 1200,723" fill="none" stroke="var(--gold)" stroke-width="4"/></svg>
<div class="abs about-frame"></div>
<div class="photo" style="left:151px;top:2538px;width:419px;height:523px;background:radial-gradient(circle at 60% 45%,#b0541a,#4a2510 45%,#120a06 80%)" role="img" aria-label="Whiskey bottle and glass with a cigar resting on a crystal ashtray"></div>
<h2 class="abs blackletter" style="left:611px;top:2585px;font-size:42px">About the Company</h2>
<div class="ornament" role="img" aria-label="Gold scroll ornament" style="left:611px;top:2654px"></div>
<div class="abs about-text">
  <p>Lorem Ipsum is simply dummy text of the printing and typesetting industry. Lorem Ipsum has been the industry's standard dummy text ever since the 1500s, when an unknown printer took a galley of type and scrambled it to make a type specimen book. It has survived not only five centuries, but also the leap into electronic typesetting, remaining essentially unchanged.</p>
  <p>It was popularised in the 1960s with the release of Typeline sheets containing Lorem Ipsum passages, and more recently with desktop publishing software like Folio Layout including versions of Lorem Ipsum.</p>
</div>
<div class="btn-outline" style="left:611px;top:2969px;width:117px;height:34px">About Us</div>

<!-- news -->
<h2 class="blackletter section-title" style="top:3262px">Letest News</h2>
<div class="ornament" role="img" aria-label="Gold scroll ornament" style="top:3332px"></div>
<article class="post" style="left:120px">
  <div class="img" role="img" aria-label="Pair of silver cufflinks on weathered wood" style="background:linear-gradient(135deg,#b5b5b5,#4a4a4a)"></div>
  <h3>Lorem Ipsum is simply dummy text of the printing and typesetting industry.</h3>
  <time>20 SEP, 2023</time>
</article>
<article class="post featured" style="left:448px">
  <div class="img" role="img" aria-label="Hand fastening a cufflink on a white shirt sleeve" style="background:linear-gradient(135deg,#1a1a1a,#5a4030 50%,#e6e6e6)"></div>
  <h3>Lorem Ipsum is simply dummy text of the printing and typesetting industry.</h3>
  <time>19 SEP, 2023</time>
</article>
<article class="post" style="left:774px">
  <div class="img" role="img" aria-label="Open humidor box filled with cigars" style="background:linear-gradient(135deg,#8a8a8a,#3a3a3a)"></div>
  <h3>Lorem Ipsum is simply dummy text of the printing and typesetting industry.</h3>
  <time>19 SEP, 2023</time>
</article>
<div class="btn-outline" style="left:541px;top:3836px;width:118px;height:34px">View All</div>

<!-- footer -->
<div class="photo footer-photo" role="img" aria-label="Dim background of stacked cigars"></div>
<svg class="abs" style="left:0;top:3940px" width="1200" height="150"><polyline points="0,138 120,9 1200,86" fill="none" stroke="var(--gold)" stroke-width="4"/></svg>
<div class="abs foot-brand"><i></i>Outlaw Cupboard</div>
<div class="abs foot-contact" style="top:4246px"><span>&#9743;</span><span style="color:var(--gold);text-decoration:underline">+01 (555) 010 274</span></div>
<div class="abs foot-contact" style="top:4278px;font-size:11.5px"><span>&#9993;</span><span>info@outlawcupboard.com</span></div>

<div class="abs foot-head" style="left:366px;top:4084px"><span class="gold">Useful</span> Link</div>
<div class="abs links">
  <div class="active">Home</div><div>About Us</div><div>Men's Jewelry</div><div>Cigar &amp; Bar</div><div>Man Cave Swag</div><div>Shop</div><div>News</div><div>Contact Us</div>
</div>

<div class="abs foot-head" style="left:610px;top:4084px"><span class="gold">Contact</span> Us</div>
<div class="field" style="left:610px;top:4133px;width:226px"><small>Name</small>John |</div>
<div class="field" style="left:853px;top:4133px;width:227px">E-mail</div>
<div class="field" style="left:610px;top:4184px;width:226px">Phone</div>
<div class="field" style="left:853px;top:4184px;width:227px">Subjects</div>
<div class="field" style="left:610px;top:4238px;width:470px;border:none">Message</div>
<div class="btn-outline" style="left:975px;top:4323px;width:105px;height:28px">Submit</div>

<div class="abs copy">Copyright &copy; 2023 <a>Outlaw Cupboard</a>. All Rights Reserved.</div>
<div class="abs legal">Terms &amp; Conditions &nbsp;&nbsp;|&nbsp;&nbsp; Privacy Policy</div>
<div class="abs social"><i></i><i></i><i></i><i></i></div>

</body>
</html>
```